Stylized brand name and package design project for mini camera

We require a stylized version of our brand "Velunkorti" (we call this a Logo) and we need a package design for our product.

We provide the package drawings (an Attached file named drawings)
This file is the old package design and is for you to get the dimensions only, please disregard all the elements and texts of this drawing.

We provide 3 product shots that need to be included in the package (see attached files named p1, p2, p3)
We provide a text file with the name of the product and the specs and phrases that need to be on the package. (the Attached file named brief)
We will provide a barcode that needs to be on the package (not attached yet)
See an example of a competing product (see the attached file named competitor)

Target Market(s)

18+ people concerned about the security of their homes, business, loved ones.

Font styles to use
Sans Serif

Colors
34a6d7
0493ce
85cae6
ffffff
6b449b

Requirements
Must have
• The elements on the brief (Logo, Products shots, text boxes)
• The main product shot should be the bigger centerpiece. with the other two products smaller.
Nice to have
• We would like to see a few backgrounds
• Products shots may (or may not) go inside white circles.

```html
<!DOCTYPE html>
<html lang="en">
<head>
<meta charset="utf-8">
<title>Velunkorti Mini Video Camera – Package</title>
<link href="https://fonts.googleapis.com/css2?family=Roboto+Condensed:wght@400;700&family=Quicksand:wght@400;500&display=swap" rel="stylesheet">
<style>
  :root {
    --bg: #2fa0cc;
    --brand-blue: #0493ce;
    --mid-blue: #34a6d7;
    --light-blue: #85cae6;
    --white: #ffffff;
    --panel-top: #e6e7e9;
    --ink: #111111;
    --band: #0d0d0d;
    --product: #1c1c1c;
  }
  * { box-sizing: border-box; margin: 0; padding: 0; }
  html, body { width: 1200px; height: 900px; overflow: hidden; }
  body { background: var(--bg); font-family: "Roboto Condensed", sans-serif; }
  .dieline { position: absolute; left: 235px; top: 120px; display: flex; height: 660px; box-shadow: 0 20px 40px rgba(0,0,0,.2); }
  .panel { position: relative; height: 660px; overflow: hidden; background: linear-gradient(180deg, var(--panel-top), var(--white) 60%); }
  .panel-side { width: 230px; border-right: 1px solid #cfd2d6; }
  .panel-front { width: 500px; }
  .panel svg.waves { position: absolute; left: 0; top: 0; }
  .brand-name { font-family: "Roboto Condensed", sans-serif; font-weight: 700; color: var(--brand-blue); letter-spacing: -0.5px; line-height: 1; }
  .tagline { font-family: "Quicksand", sans-serif; font-weight: 500; color: var(--brand-blue); line-height: 1.3; }
  .panel-side .brand-name { position: absolute; left: 12px; top: 40px; font-size: 42px; }
  .panel-side .tagline { position: absolute; left: 12px; top: 90px; font-size: 19px; }
  .contents { position: absolute; left: 16px; top: 190px; color: var(--ink); font-family: "Quicksand", sans-serif; }
  .contents h2 { font-size: 17px; font-weight: 500; margin-bottom: 10px; }
  .contents ul { list-style: none; font-family: "Roboto Condensed", sans-serif; font-size: 16px; }
  .contents li { display: flex; align-items: center; gap: 8px; margin-bottom: 4px; }
  .contents li::before { content: ""; width: 9px; height: 9px; border-radius: 50%; background: var(--ink); }
  .product-small { position: absolute; left: 18px; top: 370px; width: 130px; height: 160px; border-radius: 16px; background: radial-gradient(circle at 55% 50%, #3a3a3a, var(--product) 60%); }
  .net-weight { position: absolute; right: 12px; bottom: 28px; color: var(--white); font-size: 15px; font-family: "Quicksand", sans-serif; }
  .panel-front .brand-name { position: absolute; right: 26px; top: 48px; font-size: 54px; }
  .panel-front .tagline { position: absolute; right: 26px; top: 118px; font-size: 25px; text-align: right; }
  .product-main { position: absolute; left: 36px; top: 240px; width: 270px; height: 320px; border-radius: 28px; background: radial-gradient(circle at 58% 52%, #444, var(--product) 58%); }
  .features { position: absolute; left: 40px; right: 20px; bottom: 30px; display: flex; align-items: flex-end; color: var(--white); }
  .feature { flex: 1; display: flex; flex-direction: column; align-items: center; gap: 6px; font-size: 13px; text-transform: uppercase; }
  .feature + .feature { border-left: 2px solid var(--white); }
  .feature svg { width: 38px; height: 34px; fill: var(--white); }
  .feature .hd { font-size: 30px; font-weight: 700; line-height: 34px; text-transform: none; }
  .feature .res { letter-spacing: 1.5px; }
</style>
</head>
<body>
<main class="dieline">
  <section class="panel panel-side">
    <svg class="waves" width="230" height="660" viewBox="0 0 230 660">
      <path d="M0 430 Q120 490 230 440 L230 660 L0 660 Z" fill="var(--light-blue)"/>
      <path d="M0 455 Q120 505 230 465 L230 660 L0 660 Z" fill="var(--mid-blue)"/>
      <path d="M0 490 Q110 540 230 505 L230 660 L0 660 Z" fill="var(--band)"/>
    </svg>
    <h1 class="brand-name">VELUNKORTI</h1>
    <p class="tagline">Mini video camera<br>Full HD 1080p</p>
    <div class="contents">
      <h2>inside the box</h2>
      <ul>
        <li>1 Camera</li>
        <li>1 micro SD card</li>
        <li>1 micro SD reader</li>
        <li>1 manual book</li>
      </ul>
    </div>
    <div class="product-small" role="img" aria-label="Product photo of the black cube mini camera"></div>
    <p class="net-weight">Net wt. 500gm</p>
  </section>

  <section class="panel panel-front">
    <svg class="waves" width="500" height="660" viewBox="0 0 500 660">
      <path d="M0 520 Q280 500 500 300 L500 660 L0 660 Z" fill="var(--light-blue)"/>
      <path d="M0 545 Q290 520 500 350 L500 660 L0 660 Z" fill="var(--mid-blue)"/>
      <path d="M0 575 Q300 555 500 400 L500 660 L0 660 Z" fill="var(--band)"/>
    </svg>
    <h1 class="brand-name">VELUNKORTI</h1>
    <p class="tagline">Mini video camera<br>Full HD 1080p</p>
    <div class="product-main" role="img" aria-label="Main product photo of the black cube mini camera with infrared lights around the lens"></div>
    <div class="features">
      <div class="feature">
        <svg viewBox="0 0 38 34"><circle cx="10" cy="8" r="6"/><circle cx="22" cy="8" r="6"/><rect x="3" y="14" width="24" height="16" rx="2"/><path d="M27 19 L36 14 L36 30 L27 25 Z"/></svg>
        <span>Video</span>
      </div>
      <div class="feature">
        <svg viewBox="0 0 38 34"><circle cx="19" cy="13" r="11" fill="none" stroke="#fff" stroke-width="3"/><circle cx="19" cy="13" r="4"/><path d="M10 32 L28 32 L24 24 L14 24 Z"/></svg>
        <span>Night vision</span>
      </div>
      <div class="feature">
        <svg viewBox="0 0 38 34"><path d="M3 9 H12 L15 4 H23 L26 9 H35 V32 H3 Z"/></svg>
        <span>Pictures</span>
      </div>
      <div class="feature">
        <span class="hd">HD</span>
        <span class="res">1080P</span>
      </div>
      <div class="feature">
        <svg viewBox="0 0 38 34"><circle cx="21" cy="4" r="3.5"/><path d="M19 9 L24 9 L26 18 L31 20 L30 22 L24 20 L23 16 L21 23 L26 32 L23 33 L18 25 L14 33 L11 32 L16 22 L17 14 L13 17 L12 22 L10 21 L11 15 Z"/></svg>
        <span>Motion detecting</span>
      </div>
    </div>
  </section>
</main>
</body>
</html>
```